QuorraLink Business Card

We require a stunning business card for QuorraLink - a new digital marketing agency. The logo provided was designed by a graphic designer here on ArtHivePro.

www.quorralink-example.net - "Get more sales online"

What we do:
The business delivers website optimisation (Web design, social media strategy, digital strategies, SEO, PPC, conversion optimisation, email marketing) to get businesses more sales online.

The card must match the brand style which can be found on this website template:

http://layoutbazaar.example/item/plumline-adaptive-allpurpose-skin/full_screen_preview/7193046

It must have 'wow' factor so that you'll never forget QuorraLink - We're open to any materials, textures you think will work.

We don't want a boring run of the mill design - I can knock that up in Photoshop myself or use a template solution. It should be timeless and only need replacing should the contact details change.

The design should be eye catching, future proof, exceptionally chic, classy and oozing authority and confidence. QuorraLink services must not look cheap.

Here's some brilliant designs to point you in the right direction:

http://tidycraftz.example/30-superb-calling-cards/

The spec is for double sided, but we're open to your ideas. If it's going on an opaque or see through card, then of course a single side is preferable. Using creativity and thought on the medium for the card - shape - texture is desirable.

The strapline for the business is "Get more business online" please submit with / without strapline.
Updates

Please only submit your best 1-3 designs initially.

Target Market(s)

Business 2 Business - Local SMEs
Local professionals - Doctors, Dentists, Financials, Bespoke Retailers, Property companies - anyone with a decent budget to spend on digital marketing services and a high margin product or service to sell.

Industry/Entity Type

Graphic Designer

Requirements
Must have
• Text:
• name: Tom Walcroft
• position Digital Marketing Director
• mobile 07911 204 658
• website www.quorralink-example.net
Nice to have
• Check See http://tidycraftz.example/30-superb-calling-cards/ for ideas.
• LinkedIn and Twitter usernames if there is space and it works on the design.

```html
<!DOCTYPE html>
<html lang="en">
<head>
<meta charset="utf-8">
<title>QuorraLink Business Card</title>
<link href="https://fonts.googleapis.com/css2?family=Questrial&display=swap" rel="stylesheet">
<style>
  :root {
    --page: #e7e8ea;
    --teal: #1d4f63;
    --teal-deep: #143c4d;
    --teal-raised: #25627a;
    --coral: #e63d2c;
    --white: #ffffff;
    --muted: #c9d6dc;
  }
  html, body {
    margin: 0;
    width: 1200px;
    height: 900px;
    overflow: hidden;
    background: var(--page);
    font-family: "Questrial", "Century Gothic", sans-serif;
  }
  .canvas {
    position: relative;
    width: 1200px;
    height: 900px;
  }
  .card {
    position: absolute;
    box-shadow: 0 10px 30px rgba(0,0,0,0.18);
    overflow: hidden;
  }
  /* Front: blind-embossed wordmark */
  .card-front {
    left: 70px;
    top: 290px;
    width: 560px;
    height: 320px;
    background: var(--teal);
  }
  .front-wordmark {
    position: absolute;
    left: 0;
    right: 0;
    top: 50%;
    transform: translateY(-50%);
    text-align: center;
    font-size: 84px;
    letter-spacing: 1px;
    color: var(--teal-raised);
  }
  /* Back: contact side */
  .card-back {
    left: 740px;
    top: 110px;
    width: 380px;
    height: 665px;
    background: linear-gradient(160deg, var(--teal) 0%, var(--teal-deep) 100%);
    color: var(--white);
  }
  .contact-block {
    position: absolute;
    left: 34px;
    right: 30px;
    top: 34px;
  }
  .person-name,
  .person-role {
    font-size: 18px;
    font-weight: 400;
    letter-spacing: 0.4px;
    text-transform: uppercase;
    white-space: nowrap;
  }
  .person-name {
    margin: 0;
    color: var(--coral);
  }
  .person-role {
    margin: 3px 0 10px;
    color: var(--white);
  }
  .contact-line {
    margin: 0;
    font-size: 12px;
    line-height: 1.45;
    color: var(--muted);
    white-space: nowrap;
  }
  .brand-disc {
    position: absolute;
    left: 55px;
    top: 205px;
    width: 270px;
    height: 270px;
    border-radius: 50%;
    background: var(--coral);
    display: flex;
    align-items: center;
    justify-content: center;
  }
  .brand-name {
    font-size: 34px;
    color: var(--white);
    letter-spacing: 0.5px;
  }
  .address-block {
    position: absolute;
    left: 34px;
    bottom: 30px;
  }
  .address-line {
    margin: 0;
    font-size: 14px;
    line-height: 1.35;
    color: var(--muted);
  }
  .web-address {
    margin: 6px 0 0;
    font-size: 19px;
    color: var(--coral);
    white-space: nowrap;
  }
</style>
</head>
<body>
<main class="canvas">
  <section class="card card-front" aria-label="Business card front">
    <div class="front-wordmark">QuorraLink</div>
  </section>

  <section class="card card-back" aria-label="Business card back">
    <div class="contact-block">
      <h1 class="person-name">Tom Walcroft</h1>
      <h2 class="person-role">Digital Marketing Director</h2>
      <p class="contact-line">p. 844 210 37 19 &nbsp; m. 07911 204 658</p>
      <p class="contact-line">e. t.walcroft@quorralink-example.net</p>
    </div>

    <div class="brand-disc">
      <span class="brand-name">QuorraLink</span>
    </div>

    <div class="address-block">
      <p class="address-line">57 Mill Road</p>
      <p class="address-line">Brookvale</p>
      <p class="address-line">Leeds LS2 7QF</p>
      <p class="web-address">www.quorralink-example.net</p>
    </div>
  </section>
</main>
</body>
</html>
```